Redesign of Brochure of company services

We need a redesign a brochure. All of the content on the existing brochure correct, but the design we are not pleased with it. I will provide the previous brochure. Quiet Harbor Fields is Angolan company that provides multiple service ranging providing fruits, vegetables, fisheries, and meat to multiple industries in angola. Quiet Harbor Fields seeks to start delivering or providing their service to home owners looking for fresh products. We want a brochure design that covers all of these aspects.

Target Market(s)

Home owners, middle and upper age mothers, middle and upper class

Industry/Entity Type

Retail

Requirements
Must have
• Logo of the company and the content info
Nice to have
• It's up to you

```html
<!DOCTYPE html>
<html lang="pt">
<head>
<meta charset="utf-8">
<title>Quiet Harbor Fields – Brochura</title>
<link href="https://fonts.googleapis.com/css2?family=Arimo:ital,wght@0,400;0,700;1,700&family=Roboto+Slab:wght@700&family=Oswald:wght@600&display=swap" rel="stylesheet">
<style>
:root{
  --bg:#0a0a0a;
  --white:#ffffff;
  --ink:#111111;
  --blue:#0a86c2;
  --orange:#f6a03e;
  --green:#5e9f52;
  --green-text:#4f9a45;
  --red:#e0202a;
  --label:#0b0b0b;
  --pale:#eaf3e3;
}
*{box-sizing:border-box;margin:0;padding:0}
html,body{width:1200px;height:1200px;overflow:hidden;background:var(--bg)}
body{font-family:"Arimo",Arial,sans-serif;color:var(--ink)}
.brochure{position:absolute;left:238px;top:319px;width:808px;height:627px;background:var(--white);overflow:hidden}
.abs{position:absolute}
/* left column */
.contact{left:0;top:0;width:271px;height:85px;background:var(--white);padding:36px 0 0 26px}
.contact .phone{font-weight:700;font-size:22px;line-height:22px}
.contact .email{font-weight:700;font-size:14.5px;margin-top:2px}
.service{left:0;width:271px;padding:12px 16px 0 26px;color:var(--white)}
.service h2{font-size:14px;font-weight:700;margin-bottom:14px}
.service p{font-size:13px;line-height:14.3px}
.service.veg{top:85px;height:151px;background:var(--blue)}
.service.meat{top:236px;height:151px;background:var(--orange)}
.service.fish{top:387px;height:159px;background:var(--green)}
.field{left:0;top:546px;width:271px;height:81px;background:linear-gradient(#6f9ed8 0%,#cfe2f3 45%,#6e9b3a 62%,#2f5e1c 100%)}
/* middle */
.headline{left:271px;top:0;width:280px;height:197px;background:var(--green);color:var(--white);font-family:"Roboto Slab",Georgia,serif;font-size:18.5px;line-height:22.5px;text-align:center;padding-top:61px}
.photo{overflow:hidden}
.tag{position:absolute;background:var(--label);color:var(--white);font-weight:700;padding:0 10px;line-height:24px}
.meats{left:271px;top:197px;width:270px;height:96px;background:linear-gradient(110deg,#d9a79a,#b84a4a 45%,#e6c2b7 70%,#a4202a)}
.seafood{left:271px;top:293px;width:262px;height:70px;background:linear-gradient(100deg,#c9b39a,#8aa0b0 50%,#c0584a)}
.fruits{left:271px;top:363px;width:270px;height:103px;background:linear-gradient(100deg,#f4d23a,#f29a24 40%,#9cc23a 70%,#4a2a5a)}
.greens{left:551px;top:0;width:257px;height:181px;background:linear-gradient(120deg,#cfe6c8,#e8842a 40%,#d62a1c 65%,#4e8c2a)}
.fishes{left:541px;top:197px;width:267px;height:96px;background:linear-gradient(100deg,#4a6a3a,#9aa6b0 45%,#cfd6dc 65%,#5a6a4a)}
/* right lower */
.panel{left:533px;top:293px;width:275px;height:334px;background:radial-gradient(ellipse at 60% 80%,var(--pale) 0%,#f7fbf4 50%,var(--white) 80%)}
.brand{left:610px;top:366px;width:140px;text-align:center;font-size:22px;color:#333}
.brand .mark{display:block;width:16px;height:16px;background:#e8552a;margin:0 auto 6px}
.portrait{left:568px;top:431px;width:72px;height:72px;background:linear-gradient(#f0d6e2,#c98a8e);border:1px solid #ccc}
.quote{left:646px;top:433px;width:150px;font-size:10.4px;line-height:12px;color:#222}
.quote cite{display:block;font-weight:700;font-style:italic}
.address{left:570px;top:534px;font-size:13.5px;line-height:15px}
.address strong{font-size:14px}
.address .tel{font-weight:700;font-size:14px;margin-top:4px;margin-left:-4px}
.hours{left:271px;top:466px;width:280px;text-align:center}
.hours .open{font-family:"Oswald",Impact,sans-serif;color:var(--green-text);font-size:21px;line-height:22px;margin-top:20px}
.hours .round{font-family:"Oswald",Impact,sans-serif;color:var(--red);font-size:21px;line-height:20px}
.hours .ask{font-weight:700;font-style:italic;font-size:17px;line-height:19px;margin-top:2px}
.hours .tel{font-weight:700;font-size:20px;margin-top:6px}
</style>
</head>
<body>
<main class="brochure">
  <section class="abs contact">
    <div class="phone">+244 900 410 275</div>
    <div class="email">ines_tavares@mailbox.ao</div>
  </section>
  <section class="abs service veg">
    <h2>Hortaliças e Frutas</h2>
    <p>Fornecemos as mais variadas hortaliças, incluindo batata rena, batata doce, alface,abóbora, couve lombarda, couve repolho, couve repolho roxa,cebola, beterraba, beringela, courgette, nabo, feijão verde e milho.</p>
  </section>
  <section class="abs service meat">
    <h2>Carnes</h2>
    <p>Distribuimos carne fresca de gado ovino, caprino, bovino e suíno e apostamos em produtos de elevada qualidade que nos permitam manter padrões constantes de qualidade dos produtos e dos serviços por nós prestados.</p>
  </section>
  <section class="abs service fish">
    <h2>Peixes e Mariscos</h2>
    <p>Dispomos de uma vasta gama de peixes e mariscos incluindo pescada, salmão, bacalhau, atum, sardinha, carapau, linguado, camarão, lagostim, gambas, entre outros. Fornecemos o peixe e marisco sempre frescos.</p>
  </section>
  <div class="abs field" role="img" aria-label="Campo de milho verde sob céu azul com nuvens"></div>

  <section class="abs headline">Trazemos frescos<br>da melhor qualidade a<br>bom preço direitinho à<br>sua porta.</section>

  <div class="abs photo greens" role="img" aria-label="Cenouras, tomates, pimentos e espargos frescos">
    <span class="tag" style="right:0;top:157px;font-size:18px;padding-left:112px">HORTALIÇAS</span>
  </div>
  <div class="abs photo meats" role="img" aria-label="Cortes de carne fresca vermelha e enchidos">
    <span class="tag" style="left:0;top:64px;font-size:18px;padding-left:14px">CARNES</span>
  </div>
  <div class="abs photo fishes" role="img" aria-label="Peixes frescos sobre folhas">
    <span class="tag" style="right:0;top:64px;font-size:20px;padding-left:70px">Peixes</span>
  </div>
  <div class="abs panel"></div>
  <div class="abs photo seafood" role="img" aria-label="Mariscos e peixe vermelho">
    <span class="tag" style="left:0;top:38px;font-size:20px;padding:0 30px 0 20px;line-height:28px">Mariscos</span>
  </div>
  <div class="abs photo fruits" role="img" aria-label="Bananas, laranjas, maçãs, uvas e frutos silvestres">
    <span class="tag" style="left:0;top:68px;font-size:20px;padding:0 14px 0 22px;line-height:26px">Frutas</span>
  </div>

  <div class="abs brand"><span class="mark"></span>harborfields</div>
  <div class="abs portrait" role="img" aria-label="Retrato da gerente"></div>
  <blockquote class="abs quote">“A nossa missão é aproximar os produtores nacionais dos seus clientes finais, garantindo qualidade e consistência.”<cite>Inês Tavares - Gerente</cite></blockquote>
  <address class="abs address" style="font-style:normal">
    <strong>QUIET HARBOR FIELDS CORP</strong><br>Estamos no Morro Verde<br>Luanda, Angola
    <div class="tel">+244 900 410 275</div>
  </address>

  <section class="abs hours">
    <div class="open">ESTAMOS ABERTOS</div>
    <div class="round">24/24</div>
    <div class="ask">Não viu o que procura?<br>Ligue já para</div>
    <div class="tel">+244 900 410 275</div>
  </section>
</main>
</body>
</html>
```